Building company buisness cards

We are looking for a sharp modern new look for our business cards.
We are a New Zealand based company that specialises in house and land packages.
We have attached a photo of the current logo and would like to see if it can be improved somehow if needed.
We are open to any colours but we have chosen green at this stage.
Feel free to change the font and make the logo smarter looking.
Play with the colours and see what looks best.

We want a card that looks so good know one will want to throw it away!

Target Market(s)

Home buyers

Industry/Entity Type

Building

Contact Information for Business Card

Dorian Keswick
0217392604
dkeswick@tidewellhomecraft.co.nz
tidewellhomecraft.co.nz

Font styles to use
Serif
Sans Serif

Colors

Designer to choose colors to be used in the design.

Requirements
Must have
• Logo and company name on one side, details on the other side
Nice to have
• Color codes for the original green are HEX #4a8028, RGB(74,128,40), CMYK(42,0,69,50)
• Round corners, Raised and/or spot UV

```html
<!DOCTYPE html>
<html lang="en">
<head>
<meta charset="utf-8">
<title>Tidewell Homecraft – Business Card</title>
<link href="https://fonts.googleapis.com/css2?family=Jost:wght@700&family=Libre+Bodoni:wght@700&display=swap" rel="stylesheet">
<style>
  :root {
    --brand-green: #2e9600;
    --page-bg: #ffffff;
    --photo-sky: #e6e9ea;
    --photo-hill: #8d9686;
    --photo-house: #7a756c;
    --photo-glass: #b8b19f;
    --photo-lawn: #a3a890;
    --wash: rgba(255, 255, 255, 0.42);
  }
  * { margin: 0; padding: 0; box-sizing: border-box; }
  html, body {
    width: 1200px; height: 1200px; overflow: hidden;
    background: var(--page-bg);
  }
  .canvas { position: relative; width: 1200px; height: 1200px; }
  .card {
    position: absolute;
    width: 840px; height: 478px;
    border-radius: 16px;
    overflow: hidden;
  }
  .card--front { left: 184px; top: 104px; }
  .card--back  { left: 176px; top: 618px; }
  .card__photo {
    position: absolute; inset: 0;
    background:
      linear-gradient(var(--wash), var(--wash)),
      radial-gradient(ellipse 40% 30% at 52% 58%, var(--photo-glass) 0%, transparent 100%),
      radial-gradient(ellipse 45% 45% at 55% 45%, var(--photo-house) 0%, transparent 100%),
      linear-gradient(180deg, var(--photo-sky) 0%, var(--photo-sky) 8%, var(--photo-hill) 30%, var(--photo-house) 55%, var(--photo-lawn) 85%, var(--photo-house) 100%);
  }
  .card__band {
    position: absolute; left: 0; right: 0; bottom: 0;
    height: 30px; background: var(--brand-green);
  }
  .brand-mark {
    position: absolute; left: 345px; top: 70px;
    width: 150px; height: 150px; border-radius: 50%;
    background: var(--brand-green);
  }
  .brand-name {
    position: absolute; left: 0; right: 0; top: 264px;
    text-align: center;
    font-family: "Jost", sans-serif; font-weight: 700;
    font-size: 68px; line-height: 84px;
    color: var(--brand-green);
    letter-spacing: 0.5px;
  }
  .contact {
    position: absolute;
    font-family: "Libre Bodoni", serif; font-weight: 700;
    color: var(--brand-green);
    white-space: nowrap;
  }
  .contact--name { left: 48px; top: 44px; font-size: 32px; line-height: 40px; }
  .contact--phone {
    right: 48px; top: 44px; font-size: 33px; line-height: 40px;
    display: flex; align-items: center; gap: 4px;
  }
  .contact-lines {
    position: absolute; left: 0; right: 0; top: 352px;
    text-align: center;
    font-family: "Libre Bodoni", serif; font-weight: 700;
    font-size: 32px; line-height: 38px;
    color: var(--brand-green);
    white-space: nowrap;
  }
  .contact-lines .line { display: flex; justify-content: center; align-items: center; gap: 6px; }
  .icon { width: 32px; height: 32px; fill: none; stroke: var(--brand-green); flex: none; }
</style>
</head>
<body>
<main class="canvas">

  <section class="card card--front">
    <div class="card__photo" role="img" aria-label="Photograph of a modern two-storey timber home on a green coastal hillside, softly washed out"></div>
    <div class="brand-mark" aria-hidden="true"></div>
    <h1 class="brand-name">tidewell<br>homecraft.</h1>
    <div class="card__band"></div>
  </section>

  <section class="card card--back">
    <div class="card__photo" role="img" aria-label="Photograph of a modern two-storey timber home on a green coastal hillside, softly washed out"></div>
    <p class="contact contact--name">Dorian Keswick</p>
    <p class="contact contact--phone">
      <svg class="icon" viewBox="0 0 24 24" aria-hidden="true">
        <path d="M7 3 L10 3 L10.5 7 L8.5 8.5 Q10 14 14.5 16.5 L16 14.5 L20 15 L20 18 Q19 21 16 20.5 Q6 17 4 7 Q4 4 7 3 Z" fill="var(--brand-green)" stroke="none"/>
      </svg>
      <span>: 0217392604</span>
    </p>
    <div class="contact-lines">
      <p class="line"><span>@: dkeswick@tidewellhomecraft.co.nz</span></p>
      <p class="line">
        <svg class="icon" viewBox="0 0 24 24" stroke-width="1.6" aria-hidden="true">
          <circle cx="12" cy="12" r="10"/>
          <ellipse cx="12" cy="12" rx="4.5" ry="10"/>
          <line x1="2" y1="12" x2="22" y2="12"/>
          <path d="M4 7 H20 M4 17 H20"/>
        </svg>
        <span>: tidewellhomecraft.co.nz</span>
      </p>
    </div>
    <div class="card__band"></div>
  </section>

</main>
</body>
</html>
```